Corinne Dabney Interiors business cards

We need a DOUBLE SIDED business card design that is simple, elegant and modern. We are a rapidly growing Interior Design Firm, and our brand colours are blush pink, navy, and antique gold, so we require some or all of these colours to be used. The final design should portray elegance, simplicity, and have a modern feel. We have upload inspiration photos that have the feel we're looking for.

Industry/Entity Type

Interior Design

Contact Information for Business Card

Contact information and LOGO

Colors
EB3D1F
EC4F4E
F09395
F8D3D4
FCEDEE

Requirements
Must have
• Navy, the right shade of blush pink, and antique gold

```html
<!DOCTYPE html>
<html lang="en">
<head>
<meta charset="utf-8">
<title>Corinne Dabney Interiors – Business Card</title>
<link rel="stylesheet" href="https://fonts.googleapis.com/css2?family=Jost:wght@400;500&family=Lato:wght@400&display=swap">
<style>
  :root {
    --navy: #1d2b57;
    --gold: #8a6d2f;
    --blush: #f6d4d5;
    --blush-light: #fcedee;
    --rose: #f09395;
    --coral: #ec4f4e;
    --paper: #ffffff;
    --edge: #e6e2e2;
  }
  html, body {
    margin: 0;
    width: 1200px;
    height: 1200px;
    overflow: hidden;
    background: var(--paper);
  }
  .card {
    position: absolute;
    left: 322px;
    width: 548px;
    height: 342px;
    overflow: hidden;
    box-sizing: border-box;
  }
  .card--front { top: 186px; border: 1px solid var(--edge); background: var(--paper); }
  .card--back { top: 637px; background: var(--blush); }

  .floral-backdrop { position: absolute; inset: 0; }
  .card--front .floral-backdrop {
    background:
      radial-gradient(ellipse 120px 90px at 30% 20%, var(--blush-light) 60%, transparent 62%),
      radial-gradient(ellipse 140px 160px at 95% 45%, var(--blush-light) 60%, transparent 62%),
      radial-gradient(ellipse 160px 120px at 45% 100%, var(--blush-light) 60%, transparent 62%),
      radial-gradient(ellipse 120px 100px at 85% 100%, var(--blush-light) 60%, transparent 62%),
      var(--paper);
  }
  .card--back .floral-backdrop {
    background:
      radial-gradient(ellipse 160px 130px at 90% 45%, #fbe4e6 60%, transparent 62%),
      radial-gradient(ellipse 130px 110px at 65% 45%, #f9dfe1 60%, transparent 62%),
      radial-gradient(ellipse 110px 110px at 22% 45%, #f9e0e2 60%, transparent 62%),
      linear-gradient(135deg, #f7d6d7, var(--blush));
  }

  .brand-name {
    position: absolute;
    left: 0; right: 0;
    top: 155px;
    text-align: center;
    font-family: "Jost", sans-serif;
    font-weight: 400;
    font-size: 22px;
    letter-spacing: 0.5px;
    color: var(--gold);
    text-transform: uppercase;
  }
  .brand-mark {
    position: absolute;
    left: 259px;
    top: 112px;
    width: 30px;
    height: 30px;
    background: var(--navy);
  }

  .contact { position: absolute; inset: 0; }
  .person-name {
    position: absolute; left: 126px; top: 44px; margin: 0;
    font-family: "Jost", sans-serif; font-weight: 500; font-size: 23px;
    color: var(--navy); letter-spacing: 0.3px;
  }
  .person-role {
    position: absolute; left: 126px; top: 74px; margin: 0;
    font-family: "Lato", sans-serif; font-size: 16px; color: var(--rose);
  }
  .contact-line {
    position: absolute; left: 100px; margin: 0;
    display: flex; align-items: center; gap: 5px;
    font-family: "Lato", sans-serif; font-size: 15px; color: var(--navy);
    white-space: nowrap;
  }
  .contact-line--phone { top: 122px; font-family: "Jost", sans-serif; font-size: 17px; left: 104px; }
  .contact-line--email { top: 193px; }
  .contact-line--web { top: 218px; }
  .icon { width: 20px; height: 20px; flex: none; }
  .divider {
    position: absolute; left: 38px; width: 472px; top: 261px;
    height: 1px; background: var(--rose); border: 0; margin: 0;
  }
  .social-heading {
    position: absolute; left: 100px; top: 275px; margin: 0;
    font-family: "Lato", sans-serif; font-size: 12px; color: var(--coral);
    letter-spacing: 0.3px; text-transform: uppercase;
  }
  .social-handles {
    position: absolute; left: 100px; top: 295px;
    display: flex; align-items: center; gap: 6px;
    font-family: "Lato", sans-serif; font-size: 15px; color: var(--navy);
    white-space: nowrap;
  }
  .social-badge { width: 20px; height: 20px; background: #5a6aa8; border-radius: 3px; flex: none; }
  .social-handles .second { margin-left: 16px; }
</style>
</head>
<body>

<section class="card card--front" aria-label="Card front">
  <div class="floral-backdrop" role="img" aria-label="Soft blush pink abstract floral pattern on white"></div>
  <span class="brand-mark" aria-hidden="true"></span>
  <div class="brand-name">Corinne Dabney Interiors</div>
</section>

<section class="card card--back" aria-label="Card back">
  <div class="floral-backdrop" role="img" aria-label="Pale pink layered floral pattern"></div>
  <div class="contact">
    <h1 class="person-name">Corinne Dabney</h1>
    <p class="person-role">Principal Designer</p>

    <p class="contact-line contact-line--phone">
      <svg class="icon" viewBox="0 0 20 20" aria-hidden="true"><path d="M5 2l3 1 1 4-2 1.5c1 2.3 2.5 3.8 4.5 4.5L13 11l4 1 1 3-2 3C9 17 3 11 2 4z" fill="#ec6a6b"/></svg>
      Office # 555-014-2273
    </p>
    <p class="contact-line contact-line--email">
      <svg class="icon" viewBox="0 0 20 20" aria-hidden="true"><rect x="1" y="4" width="18" height="12" fill="#ef8e8f"/><path d="M1 4l9 7 9-7" fill="none" stroke="#fff" stroke-width="1.3"/></svg>
      corinne@cdinteriorsinc.com
    </p>
    <p class="contact-line contact-line--web">
      <svg class="icon" viewBox="0 0 20 20" aria-hidden="true"><circle cx="10" cy="10" r="9" fill="#ef8e8f"/><path d="M1 10h18M10 1c-4 4-4 14 0 18M10 1c4 4 4 14 0 18" fill="none" stroke="#fff" stroke-width="1"/></svg>
      www.corinnedabneyinteriors.com
    </p>

    <hr class="divider">
    <p class="social-heading">Find her on Pagebook</p>
    <div class="social-handles">
      <span class="social-badge" aria-hidden="true"></span>
      <span>corinnedabneyinteriors</span>
      <span class="second">corinne.dabney.interiors</span>
    </div>
  </div>
</section>

</body>
</html>
```